Harborline Security and Surveillance Business Card

Business Card Design - Company Name:Freedom Security and SurveillanceWe are a Security Systems Integrator Specializing in Security Systems/ Video Surveillance and Access Control. Our areas of expertise are:Security SystemsVideo SurveillanceAccess ControlFire Alarm SystemsNetwork CablingCellular BoostersMy input is the Front of the Card is: logo, name of Business, My Name, Phone Number, and email.Rear of Card is the 6 areas of expertise, I just dont want the front to be very busy.
Name: Tom Werner
Title: President
Email: tom@harborlinesecsys.example
website: harborlinesecsys.example

```html
<!DOCTYPE html>
<html lang="en">
<head>
<meta charset="utf-8">
<title>Harborline Security and Surveillance Business Card</title>
<link href="https://fonts.googleapis.com/css2?family=Open+Sans:wght@400;600;700&display=swap" rel="stylesheet">
<style>
  :root {
    --brand-blue: #2760ad;
    --ink-grey: #8a8d91;
    --ink-black: #1a1a1a;
    --paper: #ffffff;
    --backdrop: #e9eaec;
  }
  * { margin: 0; padding: 0; box-sizing: border-box; }
  html, body {
    width: 1200px; height: 900px; overflow: hidden;
    background: var(--backdrop);
    font-family: "Open Sans", Arial, sans-serif;
  }
  .canvas { position: relative; width: 1200px; height: 900px; }
  .card {
    position: absolute; width: 700px; height: 400px;
    box-shadow: 0 6px 18px rgba(0,0,0,0.12);
    overflow: hidden;
  }
  .card--front { left: 80px; top: 45px; background: var(--brand-blue); }
  .card--back { left: 420px; top: 475px; background: var(--paper); }

  .brand {
    display: flex; align-items: center; gap: 14px;
    font-weight: 600; letter-spacing: 2px; text-transform: uppercase;
  }
  .brand__dot { width: 16px; height: 16px; border-radius: 50%; flex: none; }
  .card--front .brand {
    position: absolute; left: 50%; top: 50%; transform: translate(-50%, -50%);
    color: var(--paper); font-size: 26px; white-space: nowrap;
  }
  .card--front .brand__dot { background: var(--paper); }

  .card--back .brand {
    position: absolute; left: 130px; top: 70px;
    color: var(--brand-blue); font-size: 19px; white-space: nowrap;
  }
  .card--back .brand__dot { background: var(--brand-blue); width: 13px; height: 13px; }

  .person {
    position: absolute; left: 150px; top: 168px; width: 170px; text-align: right;
  }
  .person__name { color: var(--brand-blue); font-weight: 700; font-size: 24px; line-height: 1.2; }
  .person__title { color: var(--ink-black); font-weight: 600; font-size: 15px; }

  .divider {
    position: absolute; left: 345px; top: 150px; width: 2px; height: 100px;
    background: var(--brand-blue);
  }
  .contacts {
    position: absolute; left: 370px; top: 150px; list-style: none;
    color: var(--ink-grey); font-size: 15.5px;
  }
  .contacts li { display: flex; align-items: center; gap: 10px; height: 33px; }
  .contacts svg { width: 15px; height: 15px; fill: var(--brand-blue); flex: none; }

  .address-band {
    position: absolute; left: 0; right: 0; bottom: 22px; height: 42px;
    background: var(--brand-blue); color: var(--paper);
    display: flex; align-items: center; justify-content: center;
    font-size: 17px; letter-spacing: 0.5px;
  }
</style>
</head>
<body>
<main class="canvas">
  <section class="card card--front" aria-label="Card front">
    <div class="brand"><span class="brand__dot"></span>Harborline Security and Surveillance</div>
  </section>

  <section class="card card--back" aria-label="Card back">
    <div class="brand"><span class="brand__dot"></span>Harborline Security and Surveillance</div>

    <div class="person">
      <div class="person__name">Tom Werner</div>
      <div class="person__title">President</div>
    </div>

    <div class="divider"></div>

    <ul class="contacts">
      <li>
        <svg viewBox="0 0 24 24" aria-hidden="true"><path d="M6.6 10.8a15.1 15.1 0 0 0 6.6 6.6l2.2-2.2a1 1 0 0 1 1-.25 11.4 11.4 0 0 0 3.6.57 1 1 0 0 1 1 1V20a1 1 0 0 1-1 1A17 17 0 0 1 3 4a1 1 0 0 1 1-1h3.5a1 1 0 0 1 1 1c0 1.25.2 2.45.57 3.57a1 1 0 0 1-.25 1z"/></svg>
        +32400118206
      </li>
      <li>
        <svg viewBox="0 0 24 24" aria-hidden="true"><path d="M3 5h18v14H3z M4 6.5v.3l8 5.2 8-5.2v-.3z" fill-rule="evenodd"/></svg>
        tom@harborlinesecsys.example
      </li>
      <li>
        <svg viewBox="0 0 24 24" aria-hidden="true"><circle cx="12" cy="12" r="10"/></svg>
        www.harborlinesecsys.example
      </li>
    </ul>

    <div class="address-band">Kerkweg 48 9900 Oostmeer</div>
  </section>
</main>
</body>
</html>
```